Gardener needs an exciting new flyer design.

I'm a passionate gardener that requires a custom flyer design for a owner operator gardening business. Design will be for a DL flyer. I'm based on the Sunshine coast in Queensland Australia. My target audience is the residential market on the Sunshine coast. Business name is Marlowe Greens. My services are, lawn mowing, weeding, Eco Friendly fertilizing, green waste removal, Mulching, tree and shrub pruning, Full garden makeovers, hedging, pressure cleaning, privacy screening, Timber deck rejuvenation, Planting, Turf preparation and installation, and much more. Free no obligation quotes, reliable and friendly service, great rates. 12 years experience. Web www.marlowegreens.com.au - Phone 0418527064 - Email doug@marlowegreens.com.au I would like the design to portray a friendly and professional approach.

Target Market(s)

Residential

Industry/Entity Type

Gardener

Font styles to use
Serif

Colors
9ccb3b
abd037
3176b5

Requirements
Must have
• my services, my logo, my contact details,

```html
<!DOCTYPE html>
<html lang="en">
<head>
<meta charset="utf-8">
<title>Marlowe Greens – DL Flyer</title>
<link rel="stylesheet" href="https://fonts.googleapis.com/css2?family=Cinzel:wght@400;600;700&family=Cormorant+Garamond:ital,wght@0,500;1,500&display=swap">
<style>
  :root {
    --green: #9ccb3b;
    --lime: #abd037;
    --blue: #3176b5;
    --deep-blue: #255f96;
    --ink-green: #2f5d1a;
    --white: #ffffff;
    --stage: #eceae4;
  }
  * { box-sizing: border-box; margin: 0; padding: 0; }
  html, body { width: 1200px; height: 842px; overflow: hidden; }
  body {
    background: var(--stage);
    font-family: "Cinzel", serif;
    position: relative;
  }
  .panel {
    position: absolute;
    top: 39px;
    width: 360px;
    height: 764px;
    overflow: hidden;
    box-shadow: 0 6px 18px rgba(0,0,0,.18);
  }
  .panel::after {
    content: "";
    position: absolute;
    inset: 8px;
    border: 1.5px solid rgba(255,255,255,.85);
    pointer-events: none;
  }
  .panel--front {
    left: 220px;
    background: linear-gradient(180deg, var(--lime) 0%, var(--green) 34%, var(--green) 62%, var(--blue) 82%, var(--deep-blue) 100%);
  }
  .panel--back {
    left: 620px;
    background: linear-gradient(180deg, var(--blue) 0%, var(--blue) 55%, var(--green) 78%, var(--lime) 100%);
  }
  .brand {
    display: flex;
    align-items: center;
    justify-content: center;
    gap: 10px;
    color: var(--ink-green);
    font-weight: 700;
    letter-spacing: .5px;
  }
  .brand__dot {
    width: 18px; height: 18px;
    border-radius: 50%;
    background: var(--ink-green);
  }
  .front__brand { margin-top: 74px; font-size: 30px; }
  .tagline {
    margin: 58px 20px 0;
    color: var(--white);
    text-align: center;
    font-size: 19px;
    line-height: 1.3;
    font-weight: 600;
  }
  .photo {
    margin: 22px 9px 0;
    height: 250px;
    background: linear-gradient(180deg, #bfe1f2 0%, #6fa849 40%, #3f7d2c 62%, #6fb23a 100%);
  }
  .front__contact {
    position: absolute;
    left: 0; right: 0; bottom: 40px;
    color: var(--white);
    text-align: center;
    font-size: 13px;
    line-height: 1.8;
  }
  .intro {
    margin: 42px 30px 0;
    color: var(--white);
    font-family: "Cormorant Garamond", serif;
    font-style: italic;
    font-size: 13px;
    line-height: 1.35;
    text-align: center;
  }
  .services__title {
    display: block;
    width: 140px;
    margin: 16px auto 10px;
    padding: 4px 0;
    border-radius: 12px;
    background: var(--green);
    color: var(--white);
    text-align: center;
    font-size: 11px;
    font-weight: 700;
    letter-spacing: 1px;
  }
  .services {
    list-style: none;
    text-align: center;
    color: var(--white);
    font-size: 12.5px;
    line-height: 1.62;
  }
  .perks {
    display: flex;
    justify-content: center;
    gap: 16px;
    margin-top: 18px;
  }
  .perk {
    width: 82px; height: 82px;
    border-radius: 50%;
    background: var(--green);
    border: 2px solid var(--white);
    color: var(--white);
    display: flex;
    align-items: center;
    justify-content: center;
    text-align: center;
    font-size: 9.5px;
    font-weight: 700;
    line-height: 1.25;
    padding: 8px;
  }
  .back__brand { margin-top: 40px; font-size: 22px; }
  .back__contact {
    margin-top: 10px;
    color: var(--ink-green);
    text-align: center;
    font-size: 12px;
    line-height: 1.6;
    font-weight: 600;
  }
</style>
</head>
<body>
  <section class="panel panel--front">
    <div class="brand front__brand"><span class="brand__dot"></span>Marlowe Greens</div>
    <p class="tagline">A beautiful garden<br>doesn't happen by itself</p>
    <div class="photo" role="img" aria-label="Photo of a lush green lawn with trees and blue sky"></div>
    <div class="front__contact">
      <p>Phone: 0418527064</p>
      <p>Email: doug@marlowegreens.com.au</p>
      <p>Web: www.marlowegreens.com.au</p>
    </div>
  </section>

  <section class="panel panel--back">
    <p class="intro">Marlowe Greens is your local garden and lawn care specialist, with a passion for quality work and an eye for the detail you deserve. My services are tailored to suit your home, your budget and your lifestyle. With 12 years of experience, I give every job the time it needs so you can simply enjoy your garden and outdoor spaces.</p>
    <span class="services__title">Our Services</span>
    <ul class="services">
      <li>Lawn Mowing</li>
      <li>Weeding</li>
      <li>Eco Friendly Fertilising</li>
      <li>Green Waste Removal</li>
      <li>Mulching</li>
      <li>Tree and Shrub Pruning</li>
      <li>Full Garden Makeovers</li>
      <li>Hedging</li>
      <li>Pressure Cleaning</li>
      <li>Privacy Screening</li>
      <li>Timber Deck Rejuvenation</li>
      <li>Planting</li>
      <li>Turf Preparation and Installation</li>
    </ul>
    <div class="perks">
      <div class="perk">Free No Obligation Quotes</div>
      <div class="perk">Reliable and Friendly Service</div>
      <div class="perk">Great Rates</div>
    </div>
    <div class="brand back__brand"><span class="brand__dot"></span>Marlowe Greens</div>
    <div class="back__contact">
      <p>Phone: 0418527064</p>
      <p>Email: doug@marlowegreens.com.au</p>
      <p>Web: www.marlowegreens.com.au</p>
    </div>
  </section>
</body>
</html>
```